Radiology Department needs a series of 3 facebook posts - similar design

We need a series of 3 posts for our facebook page, each one presenting the activity of one of 3 physicians.
The main design elements can be the same, the only thing that will change between posts will be the field of activity and name of the physician and the representative image of its activity.
If needed the design elements can be slightly different between posts for better adjustment to the representative images.
You can find as an attachment:
- Manual of institutional identity of the Hospital (Velmor Clinica)
- Our facebook cover page
- Our department video
- The representative images for each post, identified with the name of each physician
- The Institutional identity manual with the logo of "Brisa Medical School" - just for Dr Tomas Brandilo post.
So, each one of the three posts should state the name and field of activity of each physician, including somehow the corresponding representative image, and should have background innovative design elements.
Post 1:
Name of the physician: Prof. Doutor Rui Castelvo
Field of activity: Imagiologia Reumatológica e do Sistema Músculo-Esquelético
Image as an attachment
Post 2:
Name of the physician: Prof.ª Doutora Inês Barroca
Field of activity: Imagiologia Cardíaca
Image as an attachment
Post 3:
Name of the physician: Dr. Tomas Lupo
Field of activity: Tese de Doutoramento em Curso - Identificação da Lesão Cartilagínea Precoce. Com orientação do Prof. Doutor Rui Castelvo e Prof.ª Doutora Inês Sofia Carvalhal.
Image as an attachment
Just for Dr Tomas Lupo, the logo of Brisa Medical School should also be included (please check the corresponding institutional identity manual that was just added in documents).
Updates

Just for Dr Tomas Brandilo, the logo of Brisa Medical School should also be included (please check the corresponding institutional identity manual that was just added in documents).

Please note that we are just looking for 3 facebook POSTS, not facebook cover page, thanks.

Please kindly note that we are looking for facebook POST and NOT facebook cover page.

Target Market(s)

General Population

Industry/Entity Type

Health

Font styles to use
Other font styles liked:
• Check manual of institutional identity and try to approach if appropriate

Requirements
Must have
• Check project description.
Nice to have
• If the designer finds appropriate, the logo of the Hospital would be nice in all the three posts, the most simple one just stating "VelmorClinica" - please check the attached manual of institutional identity

```html
<!DOCTYPE html>
<html lang="pt">
<head>
<meta charset="utf-8">
<title>Velmor Clinica – Radiology Facebook Posts</title>
<link rel="stylesheet" href="https://fonts.googleapis.com/css2?family=Montserrat:wght@400;500;600;700;800&display=swap">
<style>
  :root {
    --sheet: #d3d3d3;
    --white: #ffffff;
    --teal: #0f6b78;
    --teal-dark: #0a5461;
    --brand-ink: #0f5e6b;
    --sun: #fbb526;
    --sun-deep: #f0a91c;
    --label-ink: #333333;
    --ink-dark: #1f1f1f;
  }
  * { box-sizing: border-box; margin: 0; padding: 0; }
  html, body { width: 778px; height: 1200px; overflow: hidden; }
  body {
    background: var(--sheet);
    font-family: "Montserrat", Arial, sans-serif;
    position: relative;
  }
  .post-label {
    position: absolute;
    left: 49px;
    font-size: 10px;
    font-weight: 600;
    color: var(--label-ink);
    writing-mode: vertical-rl;
    transform: rotate(180deg);
    letter-spacing: 0.2px;
  }
  .post {
    position: absolute;
    left: 84px;
    width: 632px;
    height: 330px;
    background: var(--white);
    overflow: hidden;
    box-shadow: 0 1px 3px rgba(0,0,0,0.25);
  }
  .post-art { position: absolute; inset: 0; width: 632px; height: 330px; }
  .brand {
    position: absolute;
    left: 26px; top: 31px;
    display: flex; align-items: center; gap: 8px;
  }
  .brand-dot {
    width: 54px; height: 54px; border-radius: 50%;
    background: var(--teal);
  }
  .brand-name {
    font-size: 28px; font-weight: 700; color: var(--brand-ink);
    letter-spacing: 0.2px;
  }
  .physician-tag {
    position: absolute;
    font-size: 12.5px;
    color: var(--brand-ink);
    text-align: center;
    white-space: nowrap;
  }
  .physician-tag strong { font-weight: 700; }
  .field {
    position: absolute;
    left: 0; width: 334px;
    text-align: center;
    color: var(--white);
    text-transform: uppercase;
    white-space: nowrap;
  }
  .field-title { font-weight: 800; letter-spacing: -0.5px; }
  .field-sub { font-weight: 700; letter-spacing: -0.3px; }
  .field-note {
    text-transform: none; font-weight: 500; letter-spacing: -0.2px;
  }
  .field-note strong { color: var(--sun); font-weight: 600; }
  .partner {
    position: absolute; left: 21px; top: 296px;
    display: flex; align-items: center; gap: 6px;
  }
  .partner-dot { width: 16px; height: 16px; border-radius: 50%; background: var(--sun); }
  .partner-name { font-size: 14px; font-weight: 700; color: var(--ink-dark); }
</style>
</head>
<body>

<!-- POST 1 -->
<div class="post-label" style="top:85px">FB POST 1</div>
<section class="post" style="top:85px">
  <svg class="post-art" viewBox="0 0 632 330" aria-hidden="false">
    <defs>
      <radialGradient id="scan-hands" cx="55%" cy="45%" r="60%">
        <stop offset="0" stop-color="#8a8a8a"/>
        <stop offset="0.55" stop-color="#3a3a3a"/>
        <stop offset="1" stop-color="#050505"/>
      </radialGradient>
    </defs>
    <polygon points="309,0 425,0 371,137 360,137" fill="var(--sun)"/>
    <polygon points="330,0 350,0 377,137 372,137" fill="var(--sun-deep)" opacity="0.5"/>
    <g role="img" aria-label="Angiographic scan of both hands in grey tones on black">
      <polygon points="425,0 632,0 632,330 294,330" fill="url(#scan-hands)"/>
    </g>
    <polygon points="632,197 632,330 577,330" fill="var(--sun)"/>
    <line x1="621" y1="247" x2="588" y2="330" stroke="var(--white)" stroke-width="3"/>
    <rect x="0" y="137" width="400" height="98" fill="var(--teal)"/>
    <rect x="0" y="235" width="400" height="54" fill="var(--teal-dark)"/>
    <polygon points="357,137 640,137 640,330 280,330" fill="var(--white)" opacity="0"/>
    <polygon points="358,137 420,137 420,289 296,289" fill="#000" opacity="0"/>
    <polygon points="359,137 372,137 290,330 277,330 296,289 312,289" fill="var(--white)" opacity="0"/>
    <polygon points="360,137 640,137 640,0 640,330 294,330 296,289" fill="none"/>
    <polygon points="359,137 425,0 425,137" fill="none"/>
    <polygon points="359,137 374,137 312,289 296,289" fill="#0c3b42"/>
    <line x1="372" y1="137" x2="290" y2="330" stroke="var(--sun)" stroke-width="3"/>
    <polygon points="28,122 318,122 312,151 22,151" fill="var(--sun)"/>
  </svg>
  <div class="brand"><span class="brand-dot"></span><span class="brand-name">VelmorClinica</span></div>
  <p class="physician-tag" style="left:30px; width:282px; top:128px">Physician: <strong>Prof. Doutor Rui Castelvo</strong></p>
  <h2 class="field field-title" style="top:160px; font-size:30px; line-height:34px">Imagiologia<br>Reumatológica</h2>
  <p class="field field-sub" style="top:238px; font-size:18px; line-height:22px">E do Sistema<br>Músculo-Esquelético</p>
</section>

<!-- POST 2 -->
<div class="post-label" style="top:446px">FB POST 2</div>
<section class="post" style="top:446px">
  <svg class="post-art" viewBox="0 0 632 330">
    <defs>
      <radialGradient id="scan-heart" cx="55%" cy="55%" r="55%">
        <stop offset="0" stop-color="#8a2a1c"/>
        <stop offset="0.5" stop-color="#5a1810"/>
        <stop offset="1" stop-color="#030303"/>
      </radialGradient>
    </defs>
    <polygon points="309,0 425,0 371,137 360,137" fill="var(--sun)"/>
    <g role="img" aria-label="Three-dimensional CT render of the heart and coronary arteries on black">
      <polygon points="425,0 632,0 632,330 294,330" fill="url(#scan-heart)"/>
    </g>
    <polygon points="632,197 632,330 577,330" fill="var(--sun)"/>
    <line x1="621" y1="247" x2="588" y2="330" stroke="var(--white)" stroke-width="3"/>
    <rect x="0" y="137" width="400" height="75" fill="var(--teal)"/>
    <rect x="0" y="212" width="400" height="64" fill="var(--teal-dark)"/>
    <polygon points="359,137 374,137 317,276 301,276" fill="#0c3b42"/>
    <rect x="400" y="137" width="0" height="0"/>
    <polygon points="374,137 640,137 640,0 425,0" fill="none"/>
    <line x1="372" y1="137" x2="290" y2="330" stroke="var(--sun)" stroke-width="3"/>
    <polygon points="28,122 318,122 312,151 22,151" fill="var(--sun)"/>
  </svg>
  <div class="brand"><span class="brand-dot"></span><span class="brand-name">VelmorClinica</span></div>
  <p class="physician-tag" style="left:26px; width:290px; top:128px">Physician: <strong>Prof.ª Doutora Inês Barroca</strong></p>
  <h2 class="field field-title" style="top:161px; font-size:38px; line-height:54px">Imagiologia<br>Cardíaca</h2>
</section>

<!-- POST 3 -->
<div class="post-label" style="top:807px">FB POST 3</div>
<section class="post" style="top:807px">
  <svg class="post-art" viewBox="0 0 632 330">
    <defs>
      <radialGradient id="scan-knee" cx="55%" cy="45%" r="60%">
        <stop offset="0" stop-color="#1a2fc8"/>
        <stop offset="0.6" stop-color="#1533d6"/>
        <stop offset="1" stop-color="#06104a"/>
      </radialGradient>
    </defs>
    <polygon points="309,0 425,0 371,137 360,137" fill="var(--sun)"/>
    <g role="img" aria-label="Colour-mapped MRI cross-section of a knee in blue tones">
      <polygon points="425,0 632,0 632,330 294,330" fill="url(#scan-knee)"/>
    </g>
    <polygon points="632,197 632,330 577,330" fill="var(--sun)"/>
    <line x1="621" y1="247" x2="588" y2="330" stroke="var(--white)" stroke-width="3"/>
    <rect x="0" y="114" width="420" height="78" fill="var(--teal)"/>
    <rect x="0" y="192" width="420" height="46" fill="var(--teal-dark)"/>
    <rect x="0" y="238" width="420" height="39" fill="var(--teal)"/>
    <polygon points="368,114 384,114 317,277 301,277" fill="#0c3b42"/>
    <polygon points="384,114 425,0 640,0 640,114" fill="none"/>
    <line x1="381" y1="114" x2="290" y2="330" stroke="var(--sun)" stroke-width="3"/>
    <polygon points="60,102 290,102 284,130 54,130" fill="var(--sun)"/>
  </svg>
  <div class="brand"><span class="brand-dot"></span><span class="brand-name">VelmorClinica</span></div>
  <p class="physician-tag" style="left:56px; width:230px; top:108px">Physician: <strong>Dr. Tomas Lupo</strong></p>
  <h2 class="field field-title" style="top:136px; font-size:22px; line-height:26px">Tese de Doutoramento<br>em Curso</h2>
  <p class="field field-sub" style="top:196px; font-size:16.5px; line-height:21px; font-weight:600">Identificação da Lesão<br>Cartilagínea Precoce.</p>
  <p class="field field-note" style="top:243px; font-size:11px; line-height:15px">Com orientação do <strong>Prof. Doutor Rui Castelvo</strong><br><strong>e Prof.ª Doutora Inês Sofia Carvalhal.</strong></p>
  <div class="partner"><span class="partner-dot"></span><span class="partner-name">Brisa Medical School</span></div>
</section>

</body>
</html>
```